Membership card design for video game arena

I need a two sided design for membership cards for my customers. It needs to have instructions on how to book on one side, and a nice catchy design for the other.

Please pull logo and whatever you desire from the website www.vornik-play.com

Industry/Entity Type

Entertainment

Contact Information for Business Card

The front must say Vornik-Play with the address and whatever design you choose. The back must have the details below

Colors

Designer to choose colors to be used in the design.

Requirements
Must have
• Frontside
• Company name address and phone number
• Backside
• Booking Instructions
• www.Vornik-Play.com/book-now
• Click on General Admission and input information
• Use code Gatepass7 to gain access
• See you there!
Nice to have
• A nice design and whatever you find is pertinent
Should not have
• Useless info

```html
<!DOCTYPE html>
<html lang="en">
<head>
<meta charset="UTF-8">
<title>Vornik-Play Membership Card</title>
<link rel="stylesheet" href="https://fonts.googleapis.com/css2?family=Work+Sans:wght@400;500;600&display=swap">
<style>
  :root {
    --bg: #161616;
    --card: #1f1f1f;
    --card-edge: #2a2a2a;
    --ink: #ffffff;
    --ink-soft: #cfcfcf;
  }
  * { box-sizing: border-box; margin: 0; padding: 0; }
  html, body {
    width: 1200px;
    height: 900px;
    overflow: hidden;
    background: var(--bg);
    font-family: "Work Sans", Arial, sans-serif;
    color: var(--ink);
  }
  .canvas {
    width: 1200px;
    height: 900px;
    display: flex;
    flex-direction: column;
    align-items: center;
    justify-content: center;
    gap: 40px;
  }
  .card {
    width: 700px;
    height: 400px;
    background: linear-gradient(135deg, var(--card) 0%, var(--card-edge) 100%);
    box-shadow: 0 10px 30px rgba(0,0,0,0.5);
    border-bottom: 4px solid var(--ink);
    position: relative;
  }
  .card--front {
    display: flex;
    flex-direction: column;
    align-items: center;
    justify-content: center;
    gap: 26px;
  }
  .brand {
    display: flex;
    align-items: center;
    gap: 16px;
  }
  .brand__dot {
    width: 48px;
    height: 48px;
    border-radius: 50%;
    background: var(--ink);
  }
  .brand__name {
    font-weight: 600;
    font-size: 40px;
    letter-spacing: 4px;
    text-transform: uppercase;
    color: var(--ink);
  }
  .front__details {
    font-size: 15px;
    letter-spacing: 1px;
    color: var(--ink-soft);
    text-align: center;
    line-height: 1.6;
  }
  .card--back {
    display: flex;
    align-items: center;
    padding: 0 44px;
  }
  .back__brand {
    width: 220px;
    flex: none;
    display: flex;
    flex-direction: column;
    align-items: center;
    gap: 22px;
  }
  .back__brand .brand__dot {
    width: 140px;
    height: 140px;
  }
  .back__brand .brand__name {
    font-size: 26px;
    letter-spacing: 3px;
  }
  .divider {
    width: 2px;
    height: 240px;
    flex: none;
    background: var(--ink);
    margin: 0 34px;
  }
  .booking { flex: 1; }
  .booking__title {
    font-weight: 500;
    font-size: 24px;
    letter-spacing: 1.5px;
    text-transform: uppercase;
  }
  .booking__subtitle {
    font-size: 14px;
    letter-spacing: 1.5px;
    text-transform: uppercase;
    color: var(--ink-soft);
    margin-top: 4px;
    margin-bottom: 16px;
  }
  .booking__steps { list-style: none; }
  .booking__step {
    display: flex;
    align-items: flex-start;
    gap: 10px;
    font-size: 15px;
    line-height: 1.4;
    margin-bottom: 9px;
  }
  .booking__num {
    flex: none;
    width: 18px;
    height: 18px;
    margin-top: 1px;
    border: 1px solid var(--ink);
    border-radius: 50%;
    font-size: 11px;
    line-height: 16px;
    text-align: center;
  }
  .booking__code { font-weight: 600; }
  .booking__signoff {
    font-weight: 500;
    font-size: 16px;
    letter-spacing: 1px;
    margin-top: 6px;
  }
</style>
</head>
<body>
<main class="canvas">
  <section class="card card--front" aria-label="Card front">
    <div class="brand">
      <span class="brand__dot"></span>
      <span class="brand__name">Vornik-Play</span>
    </div>
    <p class="front__details">2716 W Larkspur Rd, Fairhaven, FL 33990, USA<br>555.204.3918</p>
  </section>

  <section class="card card--back" aria-label="Card back">
    <div class="back__brand brand">
      <span class="brand__dot"></span>
      <span class="brand__name">Vornik-Play</span>
    </div>
    <div class="divider"></div>
    <div class="booking">
      <p class="booking__title">How to Book</p>
      <p class="booking__subtitle">Members</p>
      <ol class="booking__steps">
        <li class="booking__step"><span class="booking__num">1</span><span>Visit www.Vornik-Play.com/book-now</span></li>
        <li class="booking__step"><span class="booking__num">2</span><span>Click on General Admission and input information</span></li>
        <li class="booking__step"><span class="booking__num">3</span><span>Use code <span class="booking__code">Gatepass7</span> to gain access</span></li>
      </ol>
      <p class="booking__signoff">See you there!</p>
    </div>
  </section>
</main>
</body>
</html>
```